Home Improvement Company in need of a "Banner & Billboard Design"

I'm Looking for a Banner design 4X6 With Company Logo, Phone Number, website, Credentials and services.. I picture a charcoal/matte background i also want to look like a house shape design i will upload the sample...

I'm looking for a Billboard design to target homeowners who need Roofing Services. I need logo, number, website, KTL, Credentials and a catchy title. i will like to use the same colors for branding

Target Market(s)

Homeowners, Investors,

Industry/Entity Type

Home Improvement

Font styles to use
Decorative

Colors
00a990
5c5c5c
333333

Requirements
Must have
• All Credentials, Phone number, website, logo, logo colors, services, Eye Catchy, Direct Message, Friendly feeling,
• (614) 372 - 9058
• Roofing Gutters Painting Pressure Washing Exterior Design
Nice to have
• A catchy title, A direct message to a homeowner looking for home improvement services. noticeable
Should not have
• not Busy, no

```html
<!DOCTYPE html>
<html lang="en">
<head>
<meta charset="utf-8">
<title>Ridgeline Home Exteriors Billboard</title>
<link href="https://fonts.googleapis.com/css2?family=Open+Sans:wght@700;800&display=swap" rel="stylesheet">
<style>
  :root {
    --teal: #1a9585;
    --charcoal: #58585a;
    --paper: #ffffff;
    --stage: #eef1f2;
    --fold: #e9e9e9;
    --badge-red: #d7262c;
    --badge-blue: #1d5b9f;
  }
  * { margin: 0; padding: 0; box-sizing: border-box; }
  html, body { width: 997px; height: 1200px; overflow: hidden; }
  body { background: var(--stage); position: relative; font-family: "Open Sans", Arial, sans-serif; }

  .billboard {
    position: absolute; left: 20px; top: 280px;
    width: 957px; height: 640px; background: var(--paper);
    overflow: hidden;
  }
  .brand-panel { position: absolute; left: 0; top: 0; width: 413px; height: 500px; background: var(--paper); }
  .brand-lockup {
    position: absolute; left: 30px; right: 30px; top: 190px;
    display: flex; align-items: center; justify-content: center; gap: 16px;
  }
  .brand-mark { width: 40px; height: 40px; background: var(--teal); flex: none; }
  .brand-name {
    font-weight: 800; color: var(--teal); font-size: 36px; line-height: 1.15;
  }

  .credentials-strip {
    position: absolute; left: 0; top: 500px; width: 413px; height: 140px;
    background: linear-gradient(90deg, #e2e2e2, #f4f4f4 60%, #dcdcdc);
    display: flex; align-items: center; gap: 22px; padding-left: 44px;
  }
  .badge { display: block; }
  .badge-accredited { width: 44px; height: 72px; background: var(--badge-blue); border-radius: 3px; }
  .badge-certified { width: 160px; height: 44px; background: var(--badge-red); }
  .badge-manufacturer { width: 74px; height: 72px; background: var(--badge-red); }

  .info-panel { position: absolute; left: 413px; top: 0; width: 544px; height: 640px; background: var(--charcoal); }

  .contact-fold { position: absolute; left: 368px; top: 48px; }
  .contact-band {
    position: absolute; left: 368px; top: 85px; width: 589px; height: 150px;
    background: var(--teal); color: var(--paper); text-align: right; padding: 18px 36px 0 0;
  }
  .phone { font-size: 62px; font-weight: 800; line-height: 1; letter-spacing: 0.5px; }
  .website { font-size: 39px; font-weight: 700; line-height: 1.15; margin-top: 4px; }

  .services { position: absolute; left: 450px; top: 262px; list-style: none; }
  .service {
    display: flex; align-items: center; color: var(--paper);
    font-size: 44px; font-weight: 800; height: 67.5px;
  }
  .service-bullet { width: 14px; height: 14px; background: var(--paper); margin-right: 44px; flex: none; }
</style>
</head>
<body>
  <main class="billboard">
    <section class="brand-panel">
      <div class="brand-lockup">
        <span class="brand-mark"></span>
        <p class="brand-name">Ridgeline<br>Home Exteriors</p>
      </div>
    </section>

    <section class="credentials-strip">
      <span class="badge badge-accredited" role="img" aria-label="KTL accredited business badge"></span>
      <span class="badge badge-certified" role="img" aria-label="Certified roofing contractor badge"></span>
      <span class="badge badge-manufacturer" role="img" aria-label="Roofing manufacturer partner badge"></span>
    </section>

    <section class="info-panel"></section>

    <svg class="contact-fold" width="48" height="40" viewBox="0 0 48 40" aria-hidden="true">
      <polygon points="0,37 45,0 45,37" fill="#e9e9e9"/>
    </svg>
    <div class="contact-band">
      <p class="phone">(614) 372 - 9058</p>
      <p class="website">RidgelineExteriors.com</p>
    </div>

    <ul class="services">
      <li class="service"><span class="service-bullet"></span>Roofing</li>
      <li class="service"><span class="service-bullet"></span>Gutters</li>
      <li class="service"><span class="service-bullet"></span>Painting</li>
      <li class="service"><span class="service-bullet"></span>Pressure Washing</li>
      <li class="service"><span class="service-bullet"></span>Exterior Design</li>
    </ul>
  </main>
</body>
</html>
```